I need a business card representing my company, VELDRA, it's an artist management and design company. Complete name is "VELDRA Artist Mgmt. + Design Co." I need it to be world class and very appealing, sophisticated and artistically unique.
Updates

Posted an updated Brief please see. I need a business card representing my company, VELDRA, it's an artist management and design company. Complete name is "VELDRA Artist Mgmt. + Design Co." I need it to be world class and very appealing, sophisticated and artistically unique.

Designs look the same

Designs look the same

Target Market(s)

Advertisers, Entertainment Companies, Commercial companies

Industry/Entity Type

Advertising

Contact Information for Business Card

I need a business card representing my company, VELDRA, it's an artist management and design company. Complete name is "VELDRA Artist Mgmt. + Design Co." I need it to be world class and very appealing, sophisticated and artistically unique. One side can be VELDRA Artist Mgmt. + Design Co. and the other my name, Teodoro Lindqvist, my contact telephone: 412.638.2957, email veldraartist@plumora.net, my address: 3264 Harwell Ave. #517 Miami, FL 33184

Font styles to use
Other font styles liked:
• Calibri

Colors
ffffff
0455a3
f37122

Requirements
Must have
• "VELDRA" stand out bigger than the rest of the text.
Nice to have
• Name "VELDRA" can be centered on one side or in the corner or along side edges, just need something cool and different.
Should not have
• I am open just try to keep it clean looking

```html
<!DOCTYPE html>
<html lang="en">
<head>
<meta charset="utf-8">
<title>VELDRA Business Card</title>
<link rel="stylesheet" href="https://fonts.googleapis.com/css2?family=Ubuntu:wght@400;500;700&display=swap">
<style>
  :root {
    --paper: #ffffff;
    --brand-blue: #0455a3;
    --brand-orange: #f37122;
    --ink: #231f20;
    --backdrop: #3a3b3d;
  }
  * { margin: 0; padding: 0; box-sizing: border-box; }
  html, body {
    width: 1200px;
    height: 1000px;
    overflow: hidden;
    background: var(--backdrop);
    font-family: "Ubuntu", "Carlito", sans-serif;
    color: var(--ink);
  }
  .sheet {
    position: relative;
    width: 1200px;
    height: 1000px;
    display: flex;
    flex-direction: column;
    align-items: center;
    justify-content: center;
    gap: 50px;
  }
  .card {
    position: relative;
    width: 760px;
    height: 434px;
    background: var(--paper);
    overflow: hidden;
    box-shadow: 0 6px 18px rgba(0,0,0,0.35);
  }
  .card__art {
    position: absolute;
    inset: 0;
    width: 100%;
    height: 100%;
  }
  .band--blue { fill: var(--brand-blue); }
  .band--orange { fill: var(--brand-orange); }

  /* Front */
  .brand {
    position: absolute;
    left: 150px;
    top: 118px;
  }
  .brand__name {
    display: block;
    font-weight: 700;
    font-size: 100px;
    line-height: 1;
    letter-spacing: 2px;
    color: var(--ink);
  }
  .brand__tagline {
    margin-top: 10px;
    margin-left: 6px;
    font-weight: 500;
    font-size: 23px;
    color: var(--ink);
  }

  /* Back */
  .holder-name {
    position: absolute;
    left: 58px;
    top: 44px;
    font-weight: 700;
    font-size: 46px;
    letter-spacing: 1px;
  }
  .contact {
    position: absolute;
    left: 58px;
    top: 238px;
    font-weight: 400;
    font-size: 20px;
    line-height: 1.45;
  }
  .address {
    position: absolute;
    right: 48px;
    bottom: 52px;
    text-align: right;
    font-weight: 500;
    font-size: 21px;
    line-height: 1.4;
  }
</style>
</head>
<body>
<main class="sheet">

  <section class="card card--front" aria-label="Card front">
    <svg class="card__art" viewBox="0 0 760 434">
      <defs>
        <linearGradient id="texture-front" x1="0" y1="0" x2="1" y2="1">
          <stop offset="0" stop-color="#f4f4f4"/>
          <stop offset="1" stop-color="#e2e2e2"/>
        </linearGradient>
      </defs>
      <polygon role="img" aria-label="Light grey halftone dot texture" fill="url(#texture-front)" points="300,300 760,190 760,434 440,434"/>
      <polygon class="band--blue" points="0,0 440,0 412,22 22,22 22,150 0,176"/>
    </svg>
    <div class="brand">
      <span class="brand__name">VELDRA</span>
      <p class="brand__tagline">Artist Mgmt. + Design Co.</p>
    </div>
  </section>

  <section class="card card--back" aria-label="Card back">
    <svg class="card__art" viewBox="0 0 760 434">
      <defs>
        <linearGradient id="texture-back" x1="0" y1="0" x2="1" y2="1">
          <stop offset="0" stop-color="#e2e2e2"/>
          <stop offset="1" stop-color="#f6f6f6"/>
        </linearGradient>
      </defs>
      <polygon role="img" aria-label="Light grey halftone dot texture" fill="url(#texture-back)" points="0,0 520,0 420,120 0,200"/>
      <polygon class="band--orange" points="760,434 320,434 348,412 738,412 738,284 760,258"/>
    </svg>
    <h1 class="holder-name">Teodoro Lindqvist</h1>
    <p class="contact">
      <span class="contact__phone">412.638.2957</span><br>
      <span class="contact__email">veldraartist@plumora.net</span>
    </p>
    <p class="address">
      3264 Harwell Ave.<br>
      #517 Miami, FL 33184
    </p>
  </section>

</main>
</body>
</html>
```